Business Card Design - Cryotherapy

We need a custom created business card for our company FrostLeaf Spa. We provide whole body cryotherapy and localized cryotherapy to our clients. Please be creative.
Please see our website for idea's on design.
www.frostleafspa-example.com
Industry/Entity Type
Business
Contact Information for Business Card
Name, Position, Phone Number, Address, Website, Email
Look and feel
Each slider illustrates characteristics of the customer's brand and the style your logo design should communicate.

```html
<!DOCTYPE html>
<html lang="en">
<head>
<meta charset="utf-8">
<title>FrostLeaf Spa – Business Card</title>
<link rel="stylesheet" href="https://fonts.googleapis.com/css2?family=Roboto:wght@400;500&display=swap">
<style>
  :root {
    --page-bg: #e4e4e4;
    --card-dark: #2b2a2d;
    --card-dark-edge: #3a393d;
    --card-light: #ffffff;
    --teal: #1e9a86;
    --teal-line: #1a9fb3;
    --brand-green: #1f7e5e;
    --text-light: #ffffff;
    --text-grey: #d9d9d9;
  }
  * { box-sizing: border-box; margin: 0; padding: 0; }
  html, body { width: 1200px; height: 1200px; overflow: hidden; }
  body {
    background: var(--page-bg);
    font-family: "Roboto", Arial, sans-serif;
    position: relative;
  }
  .card {
    position: absolute;
    left: 250px;
    width: 700px;
    height: 400px;
    border-radius: 28px;
    overflow: hidden;
    box-shadow: 0 6px 18px rgba(0,0,0,0.18);
  }
  .card--back {
    top: 150px;
    background: linear-gradient(135deg, var(--card-dark-edge), var(--card-dark));
    display: flex;
    align-items: center;
    justify-content: center;
    gap: 16px;
  }
  .brand-dot { width: 22px; height: 22px; border-radius: 50%; flex-shrink: 0; }
  .card--back .brand-dot { background: var(--text-grey); }
  .card--back .brand-name {
    color: var(--text-grey);
    font-size: 40px;
    font-weight: 500;
    letter-spacing: 1px;
  }
  .card--front { top: 650px; background: var(--card-light); }
  .front-wave { position: absolute; inset: 0; width: 700px; height: 400px; }
  .front-brand {
    position: absolute;
    top: 42px; left: 150px;
    display: flex; align-items: center; gap: 14px;
  }
  .card--front .brand-dot { background: var(--teal); }
  .card--front .brand-name {
    color: var(--brand-green);
    font-size: 40px;
    font-weight: 500;
    letter-spacing: 1px;
  }
  .person {
    position: absolute;
    top: 112px; left: 230px;
    width: 180px;
    text-align: center;
    color: var(--brand-green);
  }
  .person__name { font-size: 22px; font-weight: 400; white-space: nowrap; }
  .person__title { font-size: 13px; margin-top: 2px; }
  .address {
    position: absolute;
    top: 170px; right: 40px;
    text-align: right;
    color: var(--text-light);
    font-size: 15px;
    font-style: normal;
    line-height: 1.35;
  }
  .contacts {
    position: absolute;
    left: 40px; bottom: 20px;
    list-style: none;
    color: var(--text-light);
    font-size: 15px;
    line-height: 1.5;
  }
  .contacts li { display: flex; align-items: center; gap: 12px; }
  .contacts svg { width: 15px; height: 15px; flex-shrink: 0; fill: var(--text-light); overflow: visible; }
</style>
</head>
<body>

<section class="card card--back" aria-label="Card back">
  <span class="brand-dot"></span>
  <span class="brand-name">FrostLeaf Spa</span>
</section>

<section class="card card--front" aria-label="Card front">
  <svg class="front-wave" viewBox="0 0 700 400" aria-hidden="true">
    <defs>
      <linearGradient id="tealFill" x1="0" y1="1" x2="1" y2="0">
        <stop offset="0" stop-color="#35a89a"/>
        <stop offset="1" stop-color="#16866f"/>
      </linearGradient>
    </defs>
    <path d="M0,300 C200,230 440,150 700,110" fill="none" stroke="var(--teal-line)" stroke-width="5"/>
    <path d="M0,322 C200,252 440,172 700,132 L700,400 L0,400 Z" fill="url(#tealFill)"/>
  </svg>

  <div class="front-brand">
    <span class="brand-dot"></span>
    <span class="brand-name">FrostLeaf Spa</span>
  </div>

  <div class="person">
    <p class="person__name">Your Long Name</p>
    <p class="person__title">Your Title</p>
  </div>

  <address class="address">
    420 Birchwood Lane<br>
    Suite 12 Maple Grove,<br>
    IL 60000
  </address>

  <ul class="contacts">
    <li>
      <svg viewBox="0 0 24 24"><path d="M6.6 10.8a15 15 0 0 0 6.6 6.6l2.2-2.2a1 1 0 0 1 1-.25 11.4 11.4 0 0 0 3.6.57 1 1 0 0 1 1 1V20a1 1 0 0 1-1 1A17 17 0 0 1 3 4a1 1 0 0 1 1-1h3.5a1 1 0 0 1 1 1c0 1.25.2 2.45.57 3.57a1 1 0 0 1-.25 1z"/></svg>
      (555) 014-2270
    </li>
    <li>
      <svg viewBox="0 0 24 24"><path d="M2 5h20v14H2z M2 5l10 8 10-8" fill="none" stroke="#fff" stroke-width="2"/></svg>
      info@frostleafspa-example.com
    </li>
    <li>
      <svg viewBox="0 0 24 24"><circle cx="12" cy="12" r="9" fill="none" stroke="#fff" stroke-width="2"/><path d="M3 12h18M12 3c3 3 3 15 0 18M12 3c-3 3-3 15 0 18" fill="none" stroke="#fff" stroke-width="1.5"/></svg>
      www.frostleafspa-example.com
    </li>
  </ul>
</section>

</body>
</html>
```